Bathroom, Plumbing & TIling Business

I require a business card design for me new business the 'Ashgrove Tileworks Studio', based in Melbourne, Victoria.

Specialising in bathroom refurbishments, new installations, repairs, plumbing and tiling, the Ashgrove Tileworks Studio provides a professional high-quality standard of workmanship, creating your dream.

With over 15 years’ experience in the bathroom and plumbing industry the ATS will only take payment once the job is completed to the customers’ satisfaction*. We pride ourselves on hard-work, professionalism, customer service and always delivering that high end finish you have only dreamt of.

The majority of our work, to date, has come through personal recommendation and word-of-mouth and as a family-run company we do not pressure sell or push our customers to have unnecessary works.

The Ashgrove Tileworks Studio can source products for our customers at trade price and will always quote a job realistically, and honestly, on the work and materials required. We always let the customer know how long the job will take and we will complete it within the specified time.

ATS are dedicated to fitting new bathrooms, renovations, waterproofing, shower repairs/leaks and tiling to removing and refitting bathrooms, ensuites and showers and installing plumbing systems.

The business cards for ATS need to be clean, modern and simple. White matt finish with embossed bath logo.

On side 1 of the card we require the words 'Ashgrove Tileworks Studio' to be written in the Anson font with the letter V,B and C a lot larger in size to the other letters. The letter 'y' (at the end of the word 'Company') is to follow under the title in a curved bath shape growing up and around the letter V to a shower head dripping water in to the letter 'V' which will be half filled with water. The colour for the main title is the green colour which is used in the Waterfall colour scheme on MS Publisher. The tag line, 'Creating your Dream', is to be situated in a smaller font size, underneath the main title in the Anson font and be written in black (we think).

Side 2 of the card is to have a smaller sized version of the Side 1 logo (but only saying ATS - not the full title, Ashgrove Tileworks Studio) situated at the top and contact details (again, in the Anson font underneath.

The final design should communicate high-end, high quality and professionalism of bathroom fitting and plumbing works.
Updates

Hi there

Please could you include/list some of the services, provided by ATS on the back of the card:

Bathroom Renovations

Bathroom Installations

Tiling

Shower Repairs

Plumbing

Cheers :-)

Target Market(s)

Home owners, renters, property developers, rental companies seeking anything works related to bathrooms, plumbing and tiling. Age range from 21-70.

Industry/Entity Type

Industry

Requirements
Must have
• Double sided business card
Side 1: main - title (Ashgrove Tileworks Studio), logo (bath & shower) and tag line (Creating your Dream)
Side 2: Smaller sized version of Side 1 (but only with the letters ATS - not the whole company name) and contact details:

Rowan Pelliser (Owner)
Brackenvale, 3288

Website: www.ashgrovetileworksstudio.example
Email: Rowan@ats.example
Phone: +61 491 570 156
Nice to have
• The business cards for ATS need to be clean, modern and simple. White/or off white matt finish with embossed bath logo.

Should not have
• We do not want to see any of the following on the card:

No garish colours
No clip art
No cartoon images of people, baths or plumbing tools
No small photographs of bathrooms or other 'photographic' images

```html
<!DOCTYPE html>
<html lang="en">
<head>
<meta charset="utf-8">
<title>Ashgrove Tileworks Studio – Business Card</title>
<link href="https://fonts.googleapis.com/css2?family=Poiret+One&family=Open+Sans:wght@400&display=swap" rel="stylesheet">
<style>
  :root {
    --backdrop: #cccccc;
    --card: #ffffff;
    --teal: #669c9b;
    --ink: #1a1a1a;
    --on-teal: #ffffff;
    --shadow: rgba(0, 0, 0, 0.18);
  }
  * { margin: 0; padding: 0; box-sizing: border-box; }
  html, body { width: 1200px; height: 1000px; overflow: hidden; }
  body {
    background: var(--backdrop);
    position: relative;
    font-family: "Poiret One", sans-serif;
    color: var(--ink);
  }
  .card {
    position: absolute;
    background: var(--card);
    box-shadow: 1px 2px 3px var(--shadow);
    overflow: hidden;
  }
  .card--front { left: 188px; top: 58px; width: 766px; height: 440px; }
  .card--back  { left: 187px; top: 519px; width: 770px; height: 439px; }

  .brand-name {
    position: absolute;
    left: 0; right: 0; top: 162px;
    text-align: center;
    font-family: "Poiret One", sans-serif;
    font-weight: 400;
    font-size: 60px;
    line-height: 1.2;
    letter-spacing: 1px;
    color: var(--teal);
    white-space: nowrap;
  }
  .tagline {
    position: absolute;
    left: 0; right: 0; top: 292px;
    text-align: center;
    font-family: "Poiret One", sans-serif;
    font-size: 31px;
    line-height: 1.2;
    color: var(--ink);
  }

  .brand-initials {
    position: absolute;
    left: 40px; top: 50px;
    font-family: "Poiret One", sans-serif;
    font-weight: 400;
    font-size: 128px;
    line-height: 1;
    letter-spacing: 2px;
    color: var(--teal);
  }
  .contact {
    position: absolute;
    left: 52px; top: 224px;
    font-family: "Poiret One", sans-serif;
    font-size: 22px;
    line-height: 26px;
    color: var(--ink);
    list-style: none;
    white-space: nowrap;
  }
  .contact .gap { height: 26px; }

  .services-panel {
    position: absolute;
    right: 0; top: 0;
    width: 174px; height: 100%;
    background: var(--teal);
  }
  .services {
    position: absolute;
    left: 4px; top: 226px;
    list-style: none;
    font-family: "Open Sans", sans-serif;
    font-size: 16px;
    line-height: 27.6px;
    color: var(--on-teal);
    white-space: nowrap;
  }
</style>
</head>
<body>

  <section class="card card--front" aria-label="Card front">
    <h1 class="brand-name">Ashgrove Tileworks Studio</h1>
    <p class="tagline">Creating your Dream</p>
  </section>

  <section class="card card--back" aria-label="Card back">
    <div class="brand-initials">ATS</div>
    <ul class="contact">
      <li>Rowan Pelliser (Owner)</li>
      <li>Brackenvale, 3288</li>
      <li class="gap"></li>
      <li>Website: www.ashgrovetileworksstudio.example</li>
      <li>Email: Rowan@ats.example</li>
      <li>Phone: +61 491 570 156</li>
    </ul>
    <aside class="services-panel">
      <ul class="services">
        <li>Bathroom fittings</li>
        <li>Renovations</li>
        <li>Waterproofing</li>
        <li>Shower repair</li>
        <li>Tiling</li>
        <li>Plumbing installation</li>
      </ul>
    </aside>
  </section>

</body>
</html>
```